Name our house

My wife and I just moved to a new house. We asked friends to suggest a name based on what they know about us and our interests. The winner was "The Birches": based on our love of sailing (ie leeward vs windward) and our love of champagne (ie the yeast sediment during secondary fermentation); our name is not Birch.
We want a design we can use for a name sign at the streetfront to our house. We will have it laser cut and etched from aluminium sheet so should be single colour (probably powder coated black).
We would like the name combined with some kind of relevant imagery on the sign.
The house is about 1910 design, but clean modern lines are also a possibility.
Reason: We have been away for a week, unable to provide any useful feedback in the interim, so need to extend our deadline.

```html
<!DOCTYPE html>
<html lang="en">
<head>
<meta charset="utf-8">
<title>The Birches — House Name Sign</title>
<link rel="stylesheet" href="https://fonts.googleapis.com/css2?family=Oranienbaum&display=swap">
<style>
  :root {
    --backdrop: #d9dfdf;
    --plate: #ffffff;
    --ink: #111111;
    --shadow: rgba(0, 0, 0, 0.55);
    --rose-light: #c9c9c9;
    --rose-dark: #7d7d7d;
  }
  html, body {
    margin: 0;
    padding: 0;
    width: 1200px;
    height: 1000px;
    overflow: hidden;
    background: var(--backdrop);
  }
  .name-sign {
    position: absolute;
    left: 0;
    top: 0;
    width: 1200px;
    height: 1000px;
  }
  .plate { fill: var(--plate); }
  .plate-shadow { fill: var(--shadow); filter: blur(4px); }
  .frame { fill: none; stroke: var(--ink); }
  .house-name {
    font-family: "Oranienbaum", "Times New Roman", serif;
    font-size: 190px;
    fill: var(--ink);
  }
  .compass-area { fill: url(#roseTone); }
</style>
</head>
<body>
<svg class="name-sign" viewBox="0 0 1200 1000" xmlns="http://www.w3.org/2000/svg">
  <defs>
    <radialGradient id="roseTone" cx="0.5" cy="0.7" r="0.6">
      <stop offset="0" stop-color="var(--rose-dark)"/>
      <stop offset="1" stop-color="var(--rose-light)"/>
    </radialGradient>
  </defs>

  <rect class="plate-shadow" x="36" y="365" width="1144" height="285"/>
  <rect class="plate" x="28" y="357" width="1144" height="285"/>

  <rect class="frame" x="62" y="390" width="1076" height="219" stroke-width="2"/>
  <rect class="frame" x="67" y="395" width="1066" height="209" stroke-width="1"/>

  <rect class="compass-area" x="940" y="398" width="191" height="204"
        role="img" aria-label="Engraved compass rose with radiating bearing lines and north arrow"/>

  <text class="house-name" x="95" y="578" textLength="815" lengthAdjust="spacingAndGlyphs">THE BIRCHES</text>
</svg>
</body>
</html>
```